'The Paperlanterns' - Album Artwork Needed!!

Looking for album artwork design for a new pop/rock original band from NJ called 'The Paperlanterns'. The debut EP is entitled 'Hold the Door'.

The group is a 4 piece with a lead singer/guitar player, bass player, guitar player, and drummer. There are also piano parts on the songs played by the singer. Stylistically similar to a Bright Harbor Kids/Folds the Map/Vesper kind of vibe.

We need designs for both the front and rear of the CD sleeve as well as printing on the CD itself. We're leaning towards photo based artwork that captures the intensity of our music but we are not opposed to graphic design.

If there were a mission statement and an idea we would want to convey for the band it would be fun, energetic, happy, feel good, pumped up, moving, dynamic, get people going, powerful, lively rock songs with catchy hooks.

Energy! Energy! Energy!

Give me your best work! Lets get vibrant fun and memorable.

Let me know if you have questions!

Reason: Definitely some good designs. Going to extend it for 5 days in case there are any extras. Still open....

Reason: Still trying to narrow down the right paperlanterns EP cover. Some great designs so far. We need to pick one within the next 7 days so nows the last chance. Think colorful and fun! Let me know if you h ave any questions

Hi Designers, Seen some great work! We need to send the CD off to get manufactured so we need to pick our design ASAP! We've changed this to a committed payment project. We also increased the payment amount and listed this as a featured project. Bring your best work and please view the brief first. Any questions be sure to ask!

Reason: We've increased the payment and upgraded this to a committed project. We want to see what you've got! This is our absolute deadline as the CD needs to get manufactured ASAP! Thanks!

A lot of good ideas, not sure we found the one that captures the vibe we're going for, but we definitely need to pick ASAP! Message us if you have questions! Theo

Reason: More Designs!

Designer's - great work is coming in. Please use the font: JennaSue.ttf for the band's name 'The Paperlanterns'. The rest is all open to interpretation. Remember colorful fun and energetic!

...Also we've decided to remove the last two bonus tracks so the EP is only going to be the 5 songs: 1.) The Undertow 2.) Edge of the Porch 3.) Marnie 4.) Drifters 5.) Running Late Always Felt So Right

Designers! I have uploaded a file that contains the template for the artwork. The design will need to fit these template. Theres one for the outside of the CD and another for the face of the CD. Please let me know if you have any questions! Thank you, Theo

Target Market(s)

Younger audience 16-30

Industry/Entity Type

Printing

Requirements
Must have
• Vibrant in either color or photography
Should not have
• Photos of the band members as the design.

I provided from photos so you can get an idea for the band, but I do NOT want those used as the album artwork.

Please do not use these pictures on your design!
Thanks!

```html
<!DOCTYPE html>
<html lang="en">
<head>
<meta charset="utf-8">
<title>The Paperlanterns – Hold the Door – CD Sleeve</title>
<link rel="stylesheet" href="https://fonts.googleapis.com/css2?family=Amatic+SC:wght@700&family=Kaushan+Script&family=Arimo:ital,wght@0,400;1,400&display=swap">
<style>
  :root {
    --page: #ffffff;
    --sky-deep: #26343a;
    --sky-blue: #58809a;
    --sky-haze: #a9ab8c;
    --hill-green: #51702c;
    --hill-dark: #1c2612;
    --glow-light: #c9d98f;
    --sun-yellow: #ffe27a;
    --sun-orange: #f08a2a;
    --sun-red: #d8371c;
    --moss-dark: #17200f;
    --moss-mid: #4f7a34;
    --moss-light: #a7cf86;
    --ink-light: #fff6e6;
    --ink-brown: #2b1a10;
  }
  * { margin: 0; padding: 0; box-sizing: border-box; }
  html, body {
    width: 1200px; height: 629px; overflow: hidden;
    background: var(--page);
  }
  .sleeve { position: relative; width: 1200px; height: 629px; }

  .panel {
    position: absolute; top: 28px; width: 564px; height: 568px; overflow: hidden;
  }
  .panel--front { left: 26px; }
  .panel--back { left: 611px; }

  .artwork { position: absolute; inset: 0; width: 100%; height: 100%; }

  /* Front */
  .front-title {
    position: absolute; left: 0; top: 248px; width: 564px; text-align: center;
    font-weight: normal;
  }
  .band-name {
    display: block;
    font-family: "Amatic SC", cursive;
    font-weight: 700; font-size: 28px; letter-spacing: 1px; line-height: 1;
    color: var(--ink-brown);
    margin-left: 22px;
  }
  .album-title {
    display: block;
    font-family: "Kaushan Script", cursive;
    font-size: 38px; line-height: 1.1; margin-top: 2px;
    color: var(--ink-light);
  }

  /* Back */
  .contact {
    position: absolute; left: 12px; color: var(--ink-light);
    font-family: "Arimo", Arial, sans-serif; font-size: 13px; line-height: 1;
  }
  .contact--site { top: 85px; }
  .contact--social { top: 119px; }
  .copyright {
    position: absolute; left: 9px; top: 159px; width: 160px;
    font-family: "Arimo", Arial, sans-serif; font-size: 9.6px; line-height: 16px;
    text-align: justify; color: var(--ink-light);
  }

  .tracklist { list-style: none; }
  .track {
    position: absolute; color: var(--ink-light);
    font-family: "Arimo", Arial, sans-serif; line-height: 1;
  }
  .track__num {
    display: block; font-style: italic; font-size: 11px; margin-bottom: 2px;
  }
  .track__title { display: block; white-space: nowrap; }
  .track--1 { left: 210px; top: 306px; }
  .track--1 .track__title { font-size: 19px; }
  .track--2 { left: 193px; top: 354px; }
  .track--2 .track__title { font-size: 18px; }
  .track--3 { left: 229px; top: 402px; }
  .track--3 .track__title { font-size: 33px; }
  .track--4 { left: 229px; top: 464px; }
  .track--4 .track__title { font-size: 24px; }
  .track--5 { left: 111px; top: 518px; }
  .track--5 .track__title { font-size: 17.5px; }
</style>
</head>
<body>
<main class="sleeve">

  <section class="panel panel--front" aria-label="Front cover">
    <svg class="artwork" viewBox="0 0 564 568" preserveAspectRatio="none" role="img" aria-label="Textured painted photo of a river winding between green hills under a cloudy blue sky at sunset">
      <defs>
        <linearGradient id="front-scene" x1="0" y1="0" x2="0" y2="1">
          <stop offset="0" stop-color="var(--sky-deep)"/>
          <stop offset="0.2" stop-color="var(--sky-blue)"/>
          <stop offset="0.42" stop-color="var(--sky-haze)"/>
          <stop offset="0.6" stop-color="var(--hill-green)"/>
          <stop offset="1" stop-color="var(--hill-dark)"/>
        </linearGradient>
        <radialGradient id="front-glow" cx="0.5" cy="0.78" r="0.45">
          <stop offset="0" stop-color="var(--glow-light)" stop-opacity="0.75"/>
          <stop offset="1" stop-color="var(--glow-light)" stop-opacity="0"/>
        </radialGradient>
        <radialGradient id="front-sun" cx="0.5" cy="0.6" r="0.5">
          <stop offset="0" stop-color="var(--sun-yellow)" stop-opacity="0.95"/>
          <stop offset="0.6" stop-color="#f6b14a" stop-opacity="0.8"/>
          <stop offset="1" stop-color="var(--sun-orange)" stop-opacity="0.6"/>
        </radialGradient>
      </defs>
      <rect width="564" height="568" fill="url(#front-scene)"/>
      <rect width="564" height="568" fill="url(#front-glow)"/>
      <circle cx="282" cy="230" r="154" fill="url(#front-sun)"/>
    </svg>
    <h1 class="front-title">
      <span class="band-name">The Paperlanterns</span>
      <span class="album-title">Hold the Door</span>
    </h1>
  </section>

  <section class="panel panel--back" aria-label="Back cover">
    <svg class="artwork" viewBox="0 0 564 568" preserveAspectRatio="none" role="img" aria-label="Textured painted background in deep greens and moss tones with a large red-orange sun rising from the bottom">
      <defs>
        <linearGradient id="back-moss" x1="0" y1="0" x2="1" y2="1">
          <stop offset="0" stop-color="var(--moss-dark)"/>
          <stop offset="0.35" stop-color="var(--moss-mid)"/>
          <stop offset="0.55" stop-color="var(--moss-light)"/>
          <stop offset="0.8" stop-color="var(--moss-mid)"/>
          <stop offset="1" stop-color="var(--moss-dark)"/>
        </linearGradient>
        <radialGradient id="back-sun" cx="0.4" cy="0.6" r="0.6">
          <stop offset="0" stop-color="var(--sun-red)"/>
          <stop offset="0.55" stop-color="#e2552a"/>
          <stop offset="0.85" stop-color="var(--sun-orange)"/>
          <stop offset="1" stop-color="#f3b552"/>
        </radialGradient>
      </defs>
      <rect width="564" height="568" fill="url(#back-moss)"/>
      <circle cx="284" cy="534" r="255" fill="url(#back-sun)"/>
    </svg>

    <p class="contact contact--site">WWW.PAPERLANTERNS-MUSIC.COM</p>
    <p class="contact contact--social">paperlanterns/fanpage.net</p>
    <p class="copyright">COPYRIGHT - "Lorem ipsum dolor sit amet, consectetur adipisicing elit, sed do eiusmod tempor incididunt ut labore et dolore magna aliqua. Ut enim ad minim</p>

    <ol class="tracklist">
      <li class="track track--1"><span class="track__num">01</span><span class="track__title">The Undertow</span></li>
      <li class="track track--2"><span class="track__num">02</span><span class="track__title">EDGE OF THE PORCH</span></li>
      <li class="track track--3"><span class="track__num">03</span><span class="track__title">Marnie</span></li>
      <li class="track track--4"><span class="track__num">04</span><span class="track__title">DRIFTERS</span></li>
      <li class="track track--5"><span class="track__num">05</span><span class="track__title">RUNNING LATE ALWAYS FELT SO RIGHT</span></li>
    </ol>
  </section>

</main>
</body>
</html>
```